Local Roofing/Construction company business needs new biz card design

We need a new business card design, current cards are from the start of this operation and generic at best. We are a local Construction Company (General Contractor) with a majority of our work originating from insurance claims-exterior finish work is the main focus (Roofs-Siding-Gutters etc). Heavily involved with homeowners and the low ball offers they receive from insurance company's after a insurable event takes place. I have attached some of our original logo file(s) below.

```html
<!DOCTYPE html>
<html lang="en">
<head>
<meta charset="utf-8">
<title>Stonebrook Construction – Business Card</title>
<link href="https://fonts.googleapis.com/css2?family=Poppins:wght@400;500;700&display=swap" rel="stylesheet">
<style>
  :root {
    --stage: #2a2a2a;
    --brand-green: #33d67a;
    --green-deep: #27b866;
    --card-dark: #0e1d21;
    --ink-light: #f4f4f2;
    --divider: #2c3f42;
  }
  * { margin: 0; padding: 0; box-sizing: border-box; }
  html, body {
    width: 1200px; height: 689px; overflow: hidden;
    background: var(--stage);
    font-family: "Poppins", sans-serif;
  }
  .stage {
    width: 1200px; height: 689px;
    display: flex; align-items: center; justify-content: center; gap: 56px;
  }
  .card {
    width: 525px; height: 300px;
    border-radius: 22px;
    position: relative; overflow: hidden;
  }
  /* Front */
  .card-front {
    background: var(--brand-green);
  }
  .front-pattern {
    position: absolute; inset: 0;
    background: linear-gradient(135deg, var(--brand-green) 0%, var(--green-deep) 50%, var(--brand-green) 100%);
    opacity: 0.55;
  }
  .front-badge {
    position: absolute; left: 50%; top: 50%;
    transform: translate(-50%, -50%);
    display: flex; align-items: center; gap: 10px;
    color: var(--ink-light);
    font-weight: 700; font-size: 22px; letter-spacing: 0.5px;
  }
  .badge-square {
    width: 18px; height: 18px; background: var(--ink-light);
  }
  /* Back */
  .card-back {
    background: var(--brand-green);
    padding: 7px;
  }
  .back-inner {
    width: 100%; height: 100%;
    background: var(--card-dark);
    border-radius: 16px;
    display: flex; align-items: center;
    padding: 0 28px 0 30px;
  }
  .brand-block {
    width: 200px;
    display: flex; flex-direction: column; align-items: flex-start; gap: 12px;
  }
  .brand-square {
    width: 46px; height: 46px; background: var(--brand-green); border-radius: 6px;
  }
  .brand-name {
    color: var(--brand-green);
    font-weight: 700; font-size: 24px; line-height: 1.15;
  }
  .divider {
    width: 1px; height: 170px; background: var(--divider);
    margin: 0 26px 0 18px;
  }
  .contact { color: var(--ink-light); }
  .person-name {
    color: var(--brand-green);
    font-weight: 700; font-size: 20px; text-transform: uppercase; line-height: 1.1;
  }
  .person-title { font-size: 13px; margin-bottom: 14px; }
  .contact-list { list-style: none; font-size: 12.5px; line-height: 1.7; }
  .contact-list li { display: flex; align-items: center; gap: 8px; }
  .contact-list svg { width: 12px; height: 12px; flex: none; }
  .address { font-size: 12.5px; line-height: 1.45; margin-top: 12px; padding-left: 20px; }
</style>
</head>
<body>
<main class="stage">
  <section class="card card-front">
    <div class="front-pattern" role="img" aria-label="Repeating brand mark pattern in darker green tones"></div>
    <div class="front-badge">
      <span class="badge-square"></span>
      <span>Stonebrook</span>
    </div>
  </section>

  <section class="card card-back">
    <div class="back-inner">
      <div class="brand-block">
        <span class="brand-square"></span>
        <span class="brand-name">Stonebrook<br>Construction</span>
      </div>
      <div class="divider"></div>
      <div class="contact">
        <p class="person-name">Marcus Hale</p>
        <p class="person-title">Managing Director</p>
        <ul class="contact-list">
          <li>
            <svg viewBox="0 0 24 24" fill="var(--brand-green)"><path d="M6.6 10.8a15.1 15.1 0 0 0 6.6 6.6l2.2-2.2c.3-.3.7-.4 1-.2 1.1.4 2.3.6 3.6.6.6 0 1 .4 1 1V20c0 .6-.4 1-1 1A17 17 0 0 1 3 4c0-.6.4-1 1-1h3.5c.6 0 1 .4 1 1 0 1.3.2 2.5.6 3.6.1.3 0 .7-.2 1z"/></svg>
            055-210 884 316
          </li>
          <li>
            <svg viewBox="0 0 24 24" fill="var(--brand-green)"><path d="M2 5h20v14H2zm2 2v.5l8 5 8-5V7z"/></svg>
            hello@stonebrook.com
          </li>
          <li>
            <svg viewBox="0 0 24 24" fill="none" stroke="var(--brand-green)" stroke-width="2"><circle cx="12" cy="12" r="9"/><path d="M3 12h18M12 3c3 3 3 15 0 18M12 3c-3 3-3 15 0 18"/></svg>
            www.stonebrookbuild.com
          </li>
        </ul>
        <p class="address">88, Harbor Lane, Fairview<br>45310, Ohio USA</p>
      </div>
    </div>
  </section>
</main>
</body>
</html>
```